Conference banner for Kestrel training organisation

We empower everyday heroes.
We provide training that empowers individuals to create positive change in themselves, their community, and the world.
We need a large banner design to promote the organisation at conferences and events. We are open to ideas and creativity.
It may involve creatively displaying our logo only, or it may involve our logo and a summary of our products (Kestrel training, Calm Minds Field Care).
Size: 820mm width x 1790mm height
300dpi
Target Market(s)
Educators and frontline health, community, and social workers.
Industry/Entity Type
Training
Colors
Designer to choose colors to be used in the design.

```html
<!DOCTYPE html>
<html lang="en">
<head>
<meta charset="utf-8">
<title>Kestrel House – Conference Banner</title>
<link rel="stylesheet" href="https://fonts.googleapis.com/css2?family=Open+Sans:wght@300;600;700;800&display=swap">
<style>
  :root {
    --brand-blue: #1d76bc;
    --name-blue: #2e6bb3;
    --crescent-red: #b4455a;
    --accent-pink: #f0698f;
    --white: #ffffff;
  }
  * { margin: 0; padding: 0; box-sizing: border-box; }
  html, body {
    width: 1200px;
    height: 2410px;
    overflow: hidden;
    background: var(--brand-blue);
  }
  .banner {
    position: relative;
    width: 1200px;
    height: 2410px;
    overflow: hidden;
    font-family: "Open Sans", Arial, sans-serif;
    color: var(--white);
  }
  .banner__shapes {
    position: absolute;
    inset: 0;
    width: 1200px;
    height: 2410px;
  }
  .brand {
    position: absolute;
    top: 180px;
    left: 0;
    width: 1200px;
    display: flex;
    flex-direction: column;
    align-items: center;
  }
  .brand__dot {
    width: 120px;
    height: 120px;
    border-radius: 50%;
    background: var(--name-blue);
    margin-bottom: 46px;
  }
  .brand__name {
    font-weight: 700;
    font-size: 100px;
    line-height: 1;
    letter-spacing: 3px;
    color: var(--name-blue);
  }
  .tagline {
    position: absolute;
    top: 905px;
    left: 0;
    width: 1200px;
    text-align: center;
    font-weight: 300;
    font-size: 78px;
    line-height: 128px;
  }
  .services {
    position: absolute;
    top: 1366px;
    left: 162px;
    width: 874px;
    list-style: none;
  }
  .services__item {
    height: 131px;
    margin-bottom: 82px;
    border-radius: 26px;
    background: var(--accent-pink);
    display: flex;
    align-items: center;
    justify-content: center;
    font-weight: 800;
    font-size: 50px;
    letter-spacing: 1px;
    text-transform: uppercase;
  }
  .contact {
    position: absolute;
    top: 2112px;
    left: 0;
    width: 1200px;
    text-align: center;
  }
  .contact__line {
    font-weight: 600;
    font-size: 41px;
    line-height: 62px;
  }
  .contact__web {
    font-weight: 700;
    font-size: 49px;
    line-height: 64px;
  }
</style>
</head>
<body>
<main class="banner">
  <svg class="banner__shapes" viewBox="0 0 1200 2410" aria-hidden="false">
    <defs>
      <linearGradient id="ribbonTone" x1="0" y1="0" x2="1" y2="1">
        <stop offset="0" stop-color="#6a7fb8" stop-opacity="0.35"/>
        <stop offset="0.5" stop-color="#3f5f9e" stop-opacity="0.3"/>
        <stop offset="1" stop-color="#b05a85" stop-opacity="0.35"/>
      </linearGradient>
    </defs>
    <rect class="field" width="1200" height="2410" fill="var(--brand-blue)"/>
    <g role="img" aria-label="Faint flowing ribbon decoration rising through the centre of the banner">
      <rect x="420" y="760" width="380" height="1650" rx="190" fill="url(#ribbonTone)"/>
    </g>
    <path class="crescent" d="M0 498 Q600 1006 1200 498 Z" fill="var(--crescent-red)"/>
    <path class="header-panel" d="M0 0 H1200 V498 Q600 884 0 498 Z" fill="var(--white)"/>
    <path class="footer-panel" d="M0 2095 Q600 1949 1200 2095 V2410 H0 Z" fill="var(--accent-pink)" fill-opacity="0.95"/>
  </svg>

  <header class="brand">
    <span class="brand__dot"></span>
    <h1 class="brand__name">KESTREL HOUSE</h1>
  </header>

  <p class="tagline">Fulfil Your Potential.<br>Overcome Challenges.</p>

  <ul class="services">
    <li class="services__item">Everyday Kestrel Training</li>
    <li class="services__item">Mindfulness Classes</li>
    <li class="services__item">Calm Minds Field Care</li>
  </ul>

  <footer class="contact">
    <p class="contact__line">E: Contact@KestrelHouse.com.au</p>
    <p class="contact__line">P: +61 (03) 5550 0172</p>
    <p class="contact__web">www.kestrelhousegeelong.com.au</p>
  </footer>
</main>
</body>
</html>
```